Pagewall, Blipster and Crewnest cover image design

Looking to update the pagewall, blipster and aLinkedin cover images for Halvard Ledger . website www.halvledger-example.com
https://www.crewnest-example.com/company/halvard-ledger-llc/mycompany/?viewAsMember=true
https://www.pagewall-example.com/halvledger
https://blipster-example.com/halvledger

```html
<!DOCTYPE html>
<html lang="en">
<head>
<meta charset="utf-8">
<title>Halvard Ledger – Cover Images</title>
<link href="https://fonts.googleapis.com/css2?family=Oswald:wght@400;500&family=Roboto:wght@300;400&family=Montserrat:wght@500&display=swap" rel="stylesheet">
<style>
  :root{
    --board:#a9aaae;
    --label:#dcdcde;
    --green:#4b8e3f;
    --ink:#6d6d6d;
    --paper:#ffffff;
  }
  *{margin:0;padding:0;box-sizing:border-box}
  html,body{width:1200px;height:1180px;overflow:hidden}
  body{background:var(--board);position:relative;font-family:"Roboto",sans-serif}

  .board-label{position:absolute;left:99px;color:var(--label);font:300 15px "Roboto",sans-serif}

  .cover{position:absolute;background:var(--paper);overflow:hidden;box-shadow:0 4px 8px rgba(0,0,0,.35)}
  .cover__backdrop{position:absolute;inset:0;background:linear-gradient(100deg,#eeeeee 0%,#f6f6f6 35%,#ececec 60%,#f7f7f7 100%)}
  .cover__shapes{position:absolute;inset:0}
  .cover__photo-frame{position:absolute;background:var(--paper);box-shadow:0 1px 4px rgba(0,0,0,.25)}
  .cover__photo{position:absolute;inset:4px;background:linear-gradient(160deg,#e8d6d0 0%,#cfc9c8 40%,#6a6b70 62%,#dcdcdc 80%)}
  .cover__bracket{position:absolute;border-left:2px solid var(--green);border-bottom:2px solid var(--green)}

  .brand{position:absolute;display:flex;align-items:center}
  .brand__square{background:var(--green);flex:none}
  .brand__name{font-family:"Roboto",sans-serif;font-weight:400;color:var(--ink);text-transform:uppercase;line-height:.95;letter-spacing:-.02em}

  .headline{position:absolute;font-family:"Oswald",sans-serif;font-size:inherit;font-weight:400;white-space:nowrap;line-height:1}
  .headline__ask{display:block;color:var(--ink);font-weight:400;line-height:1.2}
  .headline__offer{display:block;color:var(--green);font-weight:500;line-height:1.2}

  .benefits{position:absolute;color:var(--ink);font-family:"Roboto",sans-serif;white-space:nowrap;line-height:1.38}
  .benefits span{margin-right:.5em}

  .site-tag{position:absolute;background:var(--green);color:#fff;font-family:"Montserrat",sans-serif;font-weight:500;text-align:center;letter-spacing:1px;white-space:nowrap}

  .profile{position:absolute;border-radius:50%;background:var(--paper);box-shadow:0 3px 8px rgba(0,0,0,.4);display:flex;align-items:center;justify-content:center}
  .profile::before{content:"";position:absolute;inset:4px;border:1.5px solid var(--green);border-radius:50%}

  /* Blipster */
  .cover--blipster{left:99px;top:69px;width:953px;height:317px}
  .cover--blipster .brand{left:17px;top:14px}
  .cover--blipster .brand__square{width:40px;height:40px;margin-right:4px}
  .cover--blipster .brand__name{font-size:16px}
  .cover--blipster .headline{left:119px;top:58px}
  .cover--blipster .headline__ask{font-size:29px;line-height:1.12}
  .cover--blipster .headline__offer{font-size:44px;line-height:1.2}
  .cover--blipster .benefits{left:251px;top:197px;font-size:14px}
  .cover--blipster .site-tag{left:356px;top:269px;width:176px;height:17px;font-size:9px;line-height:17px}

  /* Crewnest */
  .cover--crewnest{left:99px;top:511px;width:1005px;height:251px}
  .cover--crewnest .brand{left:14px;top:17px}
  .cover--crewnest .brand__square{width:44px;height:44px;margin-right:3px}
  .cover--crewnest .brand__name{font-size:18px}
  .cover--crewnest .headline{left:230px;top:38px}
  .cover--crewnest .headline__ask{font-size:26px;line-height:1.13}
  .cover--crewnest .headline__offer{font-size:41px;line-height:1.15}
  .cover--crewnest .benefits{left:402px;top:150px;font-size:13.5px;line-height:1.32}
  .cover--crewnest .site-tag{left:486px;top:213px;width:162px;height:15px;font-size:8.5px;line-height:15px}

  /* Pagewall */
  .cover--pagewall{left:99px;top:903px;width:542px;height:200px}
  .cover--pagewall .brand{left:12px;top:11px}
  .cover--pagewall .brand__square{width:22px;height:22px;margin-right:2px}
  .cover--pagewall .brand__name{font-size:9px}
  .cover--pagewall .headline{left:61px;top:45px}
  .cover--pagewall .headline__ask{font-size:16.5px;line-height:1.1}
  .cover--pagewall .headline__offer{font-size:25px;line-height:1.2}
  .cover--pagewall .benefits{left:135px;top:115px;font-size:8.2px;line-height:1.34}
  .cover--pagewall .site-tag{left:196px;top:155px;width:96px;height:9px;font-size:5.2px;line-height:9px;letter-spacing:.6px}

  .profile--blipster{left:165px;top:300px;width:148px;height:148px}
  .profile--crewnest{left:172px;top:688px;width:152px;height:152px}
  .profile--pagewall{left:131px;top:1044px;width:104px;height:104px}
  .profile .brand{position:relative}
  .profile--blipster .brand__square{width:32px;height:32px;margin-right:3px}
  .profile--blipster .brand__name{font-size:13px}
  .profile--crewnest .brand__square{width:32px;height:32px;margin-right:3px}
  .profile--crewnest .brand__name{font-size:13px}
  .profile--pagewall .brand__square{width:22px;height:22px;margin-right:2px}
  .profile--pagewall .brand__name{font-size:9px}
</style>
</head>
<body>

<p class="board-label" style="top:36px">Blipster Cover</p>

<section class="cover cover--blipster">
  <div class="cover__backdrop" role="img" aria-label="Faded office photo of an invoice on a monitor and a desk"></div>
  <svg class="cover__shapes" viewBox="0 0 953 317" width="953" height="317" role="img" aria-label="Green-tinted photo of office folders and a person writing">
    <defs><linearGradient id="tw-green" x1="0" y1="0" x2="1" y2="1"><stop offset="0" stop-color="#5eab50"/><stop offset="1" stop-color="#4a9540"/></linearGradient></defs>
    <polygon points="627,0 953,0 953,317 831,317" fill="url(#tw-green)"/>
    <line x1="610" y1="0" x2="814" y2="317" stroke="var(--green)" stroke-width="3"/>
  </svg>
  <div class="cover__photo-frame" style="left:664px;top:120px;width:166px;height:164px"><div class="cover__photo" role="img" aria-label="Hand pressing keys on a calculator"></div></div>
  <div class="cover__bracket" style="left:661px;top:238px;width:53px;height:51px"></div>
  <div class="brand"><span class="brand__square"></span><span class="brand__name">Halvard<br>Ledger</span></div>
  <h2 class="headline"><span class="headline__ask">Are You Tired Of<br>Banking Your Customers?</span><span class="headline__offer">Get Fast Invoice Payments!</span></h2>
  <p class="benefits"><span>• Low Fixed Fees</span><span>• No Contract Period,</span><br><span>• Same Day Funding</span><span>• Credit and Collection Management,</span><br><span>• 24/7 Online Monitoring</span><span>• And Much More!</span></p>
  <p class="site-tag">www.halvledger-example.com</p>
</section>
<div class="profile profile--blipster"><div class="brand"><span class="brand__square"></span><span class="brand__name">Halvard<br>Ledger</span></div></div>

<p class="board-label" style="top:487px">Crewnest Cover</p>

<section class="cover cover--crewnest">
  <div class="cover__backdrop" role="img" aria-label="Faded office photo of an invoice on a monitor and a desk"></div>
  <svg class="cover__shapes" viewBox="0 0 1005 251" width="1005" height="251" role="img" aria-label="Green-tinted photo of office folders and a person writing">
    <defs><linearGradient id="li-green" x1="0" y1="0" x2="1" y2="1"><stop offset="0" stop-color="#5eab50"/><stop offset="1" stop-color="#4a9540"/></linearGradient></defs>
    <polygon points="748,0 1005,0 1005,251 909,251" fill="url(#li-green)"/>
    <line x1="732" y1="0" x2="893" y2="251" stroke="var(--green)" stroke-width="3"/>
  </svg>
  <div class="cover__photo-frame" style="left:776px;top:95px;width:130px;height:130px"><div class="cover__photo" role="img" aria-label="Hand pressing keys on a calculator"></div></div>
  <div class="cover__bracket" style="left:774px;top:187px;width:42px;height:41px"></div>
  <div class="brand"><span class="brand__square"></span><span class="brand__name">Halvard<br>Ledger</span></div>
  <h2 class="headline"><span class="headline__ask">Are You Tired Of<br>Banking Your Customers?</span><span class="headline__offer">Get Fast Invoice Payments!</span></h2>
  <p class="benefits"><span>• Low Fixed Fees</span><span>• No Contract Period,</span><br><span>• Same Day Funding</span><span>• Credit and Collection Management,</span><br><span>• 24/7 Online Monitoring</span><span>• And Much More!</span></p>
  <p class="site-tag">www.halvledger-example.com</p>
</section>
<div class="profile profile--crewnest"><div class="brand"><span class="brand__square"></span><span class="brand__name">Halvard<br>Ledger</span></div></div>

<p class="board-label" style="top:875px">Pagewall Cover</p>

<section class="cover cover--pagewall">
  <div class="cover__backdrop" role="img" aria-label="Faded office photo of an invoice on a monitor and a desk"></div>
  <svg class="cover__shapes" viewBox="0 0 542 200" width="542" height="200" role="img" aria-label="Green-tinted photo of office folders and a person writing">
    <defs><linearGradient id="fb-green" x1="0" y1="0" x2="1" y2="1"><stop offset="0" stop-color="#5eab50"/><stop offset="1" stop-color="#4a9540"/></linearGradient></defs>
    <polygon points="335,0 542,0 542,200 467,200" fill="url(#fb-green)"/>
    <line x1="323" y1="0" x2="455" y2="200" stroke="var(--green)" stroke-width="2"/>
  </svg>
  <div class="cover__photo-frame" style="left:359px;top:77px;width:104px;height:104px"><div class="cover__photo" style="inset:3px" role="img" aria-label="Hand pressing keys on a calculator"></div></div>
  <div class="cover__bracket" style="left:358px;top:145px;width:33px;height:37px;border-width:1.5px"></div>
  <div class="brand"><span class="brand__square"></span><span class="brand__name">Halvard<br>Ledger</span></div>
  <h2 class="headline"><span class="headline__ask">Are You Tired Of<br>Banking Your Customers?</span><span class="headline__offer">Get Fast Invoice Payments!</span></h2>
  <p class="benefits"><span>• Low Fixed Fees</span><span>• No Contract Period,</span><br><span>• Same Day Funding</span><span>• Credit and Collection Management,</span><br><span>• 24/7 Online Monitoring</span><span>• And Much More!</span></p>
  <p class="site-tag">www.halvledger-example.com</p>
</section>
<div class="profile profile--pagewall"><div class="brand"><span class="brand__square"></span><span class="brand__name">Halvard<br>Ledger</span></div></div>

</body>
</html>
```